bluegum voyages

We provide boar charter for :Fishing/whale watching and diving in Sydney Harbour providing for 12 passengersI have yet to have web page made but want to make logo first then do web page later. So I want to be able to edit and add this site to card later

Contact Information for Business Card

Captain Art (Doc) Wigellphone no 0457710098email awigell4@gmail.comCompany name Marlow Outings Pty Ltd in association with far reef cruises

Font styles to use
Serif

Requirements
Nice to have
• perhaps a photo of boat and some stick diagrams of fishing.whales and diviving

```html
<!DOCTYPE html>
<html lang="en">
<head>
<meta charset="utf-8">
<title>Marlow Outings Pty Ltd — Business Cards</title>
<link href="https://fonts.googleapis.com/css2?family=Noto+Serif:wght@400;700&display=swap" rel="stylesheet">
<style>
  :root {
    --backdrop: #3a3b3f;
    --frame-blue: #1f80c8;
    --card-blue: #1357a1;
    --ink-white: #ffffff;
    --ink-soft: #dfe9f5;
    --rule: #7fa6d3;
    --icon-blue: #5fb8f0;
    --art-paper: #f6f5f1;
    --art-paper-shade: #e6e3da;
    --photo-sky: #6f9bd0;
    --photo-sky-light: #b9cde6;
    --photo-hull: #eef1f4;
    --photo-shore: #7d7a6a;
    --photo-water: #8fa9b8;
  }
  * { box-sizing: border-box; margin: 0; padding: 0; }
  html, body { width: 1200px; height: 1000px; overflow: hidden; }
  body {
    background: var(--backdrop);
    font-family: "Noto Serif", Georgia, serif;
    color: var(--ink-white);
    position: relative;
  }
  .card {
    position: absolute;
    left: 300px;
    width: 600px;
    height: 343px;
    background: var(--frame-blue);
    padding: 14px;
    box-shadow: 0 10px 24px rgba(0,0,0,0.35);
  }
  .card--front { top: 120px; }
  .card--back { top: 537px; padding: 0; }
  .card__inner {
    width: 100%;
    height: 100%;
    background: var(--card-blue);
    display: flex;
  }
  .card__art {
    width: 250px;
    height: 100%;
    background:
      radial-gradient(ellipse 70% 40% at 50% 35%, var(--art-paper) 0%, var(--art-paper) 60%, transparent 100%),
      radial-gradient(ellipse 60% 30% at 55% 75%, #efe8e6 0%, transparent 100%),
      linear-gradient(180deg, var(--art-paper) 0%, var(--art-paper-shade) 100%);
  }
  .card__info {
    flex: 1;
    padding: 26px 24px 20px 26px;
  }
  .brand { text-align: center; }
  .brand__name {
    font-weight: 700;
    font-size: 21px;
    letter-spacing: 0.5px;
    line-height: 1.1;
    text-transform: uppercase;
    white-space: nowrap;
  }
  .brand__suffix {
    font-weight: 700;
    font-size: 12px;
    letter-spacing: 1px;
    text-transform: uppercase;
  }
  .captain {
    text-align: center;
    font-weight: 700;
    font-size: 14px;
    margin-top: 22px;
    white-space: nowrap;
  }
  .contact-row {
    display: flex;
    justify-content: center;
    gap: 12px;
    font-size: 12.5px;
    margin-top: 10px;
    color: var(--ink-soft);
    white-space: nowrap;
  }
  .divider {
    border: none;
    border-top: 1px solid var(--rule);
    margin: 12px 10px 14px;
  }
  .services { list-style: none; }
  .services__item {
    display: flex;
    align-items: flex-start;
    gap: 10px;
    font-size: 13px;
    line-height: 1.35;
    margin-bottom: 12px;
    color: var(--ink-soft);
  }
  .services__icon { flex: none; margin-top: 3px; }

  .card--back .card__inner { background: var(--frame-blue); }
  .card__photos {
    width: 270px;
    height: 100%;
    display: flex;
    flex-direction: column;
  }
  .card__photo { flex: 1; }
  .card__photo--underway {
    background: linear-gradient(180deg,
      var(--photo-sky) 0%, var(--photo-sky-light) 28%,
      var(--photo-shore) 40%, var(--photo-hull) 52%,
      #ffffff 70%, var(--photo-water) 100%);
  }
  .card__photo--moored {
    background: linear-gradient(180deg,
      var(--photo-sky-light) 0%, var(--photo-sky) 30%,
      var(--photo-hull) 48%, #ffffff 72%,
      #5c6f78 100%);
  }
  .card__panel {
    flex: 1;
    margin: 14px 14px 14px 0;
    background: var(--card-blue);
    padding: 40px 20px 0 24px;
  }
  .card__panel .brand__name { font-size: 24px; }
  .card__panel .brand__suffix { font-size: 13px; }
  .signature {
    display: flex;
    align-items: center;
    gap: 12px;
    margin-top: 50px;
  }
  .signature__captain { font-weight: 700; font-size: 17px; white-space: nowrap; }
  .signature__rule { width: 1px; height: 44px; background: var(--ink-soft); flex: none; }
  .signature__contact { font-size: 14px; line-height: 1.5; color: var(--ink-soft); white-space: nowrap; }
</style>
</head>
<body>

<section class="card card--front" aria-label="Business card front">
  <div class="card__inner">
    <div class="card__art" role="img" aria-label="Line sketch of a spouting whale and a figure fishing with a rod"></div>
    <div class="card__info">
      <div class="brand">
        <div class="brand__name">Marlow Outings</div>
        <div class="brand__suffix">Pty Ltd</div>
      </div>
      <p class="captain">Captain Len</p>
      <div class="contact-row">
        <span>0468231594</span>
        <span>lpruntel7@tidewake.net</span>
      </div>
      <hr class="divider">
      <ul class="services">
        <li class="services__item">
          <svg class="services__icon" width="16" height="12" viewBox="0 0 16 12" aria-hidden="true"><circle cx="8" cy="6" r="5" fill="var(--icon-blue)"/></svg>
          <span>Fishing/whale watching and diving in Sydney Harbour</span>
        </li>
        <li class="services__item">
          <svg class="services__icon" width="16" height="12" viewBox="0 0 16 12" aria-hidden="true"><circle cx="8" cy="6" r="5" fill="var(--icon-blue)"/></svg>
          <span>Providing for 12 passengers</span>
        </li>
      </ul>
    </div>
  </div>
</section>

<section class="card card--back" aria-label="Business card back">
  <div class="card__inner">
    <div class="card__photos">
      <div class="card__photo card__photo--underway" role="img" aria-label="Photo of the white charter boat under way on the harbour"></div>
      <div class="card__photo card__photo--moored" role="img" aria-label="Photo of the white charter boat moored at the marina"></div>
    </div>
    <div class="card__panel">
      <div class="brand">
        <div class="brand__name">Marlow Outings</div>
        <div class="brand__suffix">Pty Ltd</div>
      </div>
      <div class="signature">
        <span class="signature__captain">Captain Len</span>
        <span class="signature__rule"></span>
        <div class="signature__contact">
          <div>0468231594</div>
          <div>lpruntel7@tidewake.net</div>
        </div>
      </div>
    </div>
  </div>
</section>

</body>
</html>
```